Logo alteration and design business card.

I want to make minor alterations to a logo that has already been designed and use the modified logo as part of the design of the business card.

Alterations to be made are as follows:
16-6240 TPX For the top green and bottom green dot.
16-4535 TPX For the Bottom blue and top blue dot
13-0220 TPX For the green outline.
13-5313 TPX For the middle line and the writing.

Particulars such as name, phone number and email to be generic for now so we can update and individualize them later. Website is www.orbivale.com.au

Target Market(s)

Men and Women 25-35 interested in ecofriendly/green products that have a positive vibe and message.

Industry/Entity Type

Business

Font styles to use
Script

Colors
0492cd
85cae6
00a98f
86cfc6

Requirements
Must have
• The modified Lumora Vista logo.
Nice to have
• We're looking for a design that is either nature based eg. bamboo, birds, trees, water, natural scenery etc. or something eg. spacey, stars, galaxy, universe etc. a positive/happy feeling to it that is quite simple and not over loaded with imagery.

```html
<!DOCTYPE html>
<html lang="en">
<head>
<meta charset="utf-8">
<title>Lumora Vista – Business Card</title>
<link rel="stylesheet" href="https://fonts.googleapis.com/css2?family=Open+Sans:wght@400;700&display=swap">
<style>
  :root {
    --backdrop: #2a2a2a;
    --card-white: #ffffff;
    --leaf-green: #86c21e;
    --sky-blue: #0a7cc4;
    --sky-light: #7fc8ef;
    --grass-dark: #3f7f14;
    --grass-light: #8cc63f;
    --ink: #222222;
    --ink-soft: #444444;
  }
  * { box-sizing: border-box; margin: 0; padding: 0; }
  html, body {
    width: 1200px;
    height: 1077px;
    overflow: hidden;
    background: var(--backdrop);
    font-family: "Open Sans", Arial, sans-serif;
  }
  .canvas { position: relative; width: 1200px; height: 1077px; }

  .card {
    position: absolute;
    left: 294px;
    width: 582px;
    overflow: hidden;
    box-shadow: 0 6px 18px rgba(0,0,0,0.55);
  }

  /* Front */
  .card-front { top: 100px; height: 420px; }
  .front-scene {
    position: absolute; inset: 0;
    background: linear-gradient(180deg,
      var(--sky-blue) 0%, var(--sky-light) 40%, #d9f0f7 47%,
      var(--grass-light) 52%, #6aa52a 70%, var(--grass-dark) 100%);
  }
  .front-brand {
    position: absolute; inset: 0;
    display: flex; align-items: center; justify-content: center; gap: 18px;
  }
  .brand-dot { border-radius: 50%; flex: none; }
  .front-brand .brand-dot { width: 54px; height: 54px; background: var(--card-white); }
  .front-brand .brand-name {
    font-size: 46px; font-weight: 400; color: var(--card-white); letter-spacing: 0.5px;
  }

  /* Back */
  .card-back { top: 558px; height: 415px; background: var(--card-white); }
  .back-brand {
    position: absolute; left: 47px; top: 60px;
    display: flex; align-items: center; gap: 14px;
  }
  .back-brand .brand-dot { width: 44px; height: 44px; background: var(--leaf-green); }
  .back-brand .brand-name { font-size: 34px; color: var(--leaf-green); }

  .contact-divider {
    position: absolute; left: 296px; top: 268px;
    width: 1px; height: 111px; background: var(--sky-blue);
  }
  .contact {
    position: absolute; left: 312px; top: 266px;
    color: var(--ink-soft); font-size: 13px; line-height: 17px;
  }
  .contact-name {
    color: var(--ink); font-weight: 700; font-size: 14px; letter-spacing: 1px;
    margin-bottom: 16px;
  }
  .band-green {
    position: absolute; left: 0; bottom: 0;
    width: 296px; height: 22px; background: var(--leaf-green);
  }
  .band-blue {
    position: absolute; left: 296px; right: 0; bottom: 0; height: 36px;
    background: var(--sky-blue);
    display: flex; align-items: center; justify-content: center;
    color: var(--card-white); font-size: 16px; letter-spacing: 3px;
  }
</style>
</head>
<body>
<main class="canvas">
  <section class="card card-front">
    <div class="front-scene" role="img" aria-label="Nature photo: blue sky over green grass meadow with rippling water"></div>
    <div class="front-brand">
      <span class="brand-dot"></span>
      <span class="brand-name">Lumora Vista</span>
    </div>
  </section>

  <section class="card card-back">
    <div class="back-brand">
      <span class="brand-dot"></span>
      <span class="brand-name">Lumora Vista</span>
    </div>
    <div class="contact-divider"></div>
    <div class="contact">
      <p class="contact-name">yourname</p>
      <p>your address</p>
      <p>+62 271 5550148</p>
      <p>contact number</p>
    </div>
    <div class="band-green"></div>
    <div class="band-blue">orbivale.com</div>
  </section>
</main>
</body>
</html>
```